VELNUKA Promotions - Business Card Design Project

We are looking for a classy business cards for Promotion Company based in Toronto, Canada named Velnuka Promotions.

Velnuka Promotions has an idea and vision to set high standard, be EXCLUSIVE and attract a group of people that will follow us through events we promote (night clubs, brand promotions, music events, and sport events)

We want to present a high standards and classy image to the others...
Updates

Target Market(s)

male/female age 25-40 Target: business owners young entrepreneur - clubing industry - media industry - promotion industry - marketing media industry

Industry/Entity Type

Events

Requirements
Must have
• business cards should be classy, make people feel exclusive , make people react ..

```html
<!DOCTYPE html>
<html lang="en">
<head>
<meta charset="utf-8">
<title>Velnuka Promotions – Business Card</title>
<link rel="stylesheet" href="https://fonts.googleapis.com/css2?family=Source+Sans+3:wght@400;700&display=swap">
<style>
  :root {
    --card-black: #000000;
    --page-white: #ffffff;
    --brand-cyan: #3ff2f2;
    --text-white: #ffffff;
  }
  html, body {
    margin: 0;
    padding: 0;
    width: 1200px;
    height: 751px;
    overflow: hidden;
    background: var(--page-white);
  }
  .business-card {
    position: relative;
    width: 1200px;
    height: 751px;
    background: var(--card-black);
    border-radius: 0 64px 0 64px;
    font-family: "Source Sans 3", "Myriad Pro", Arial, sans-serif;
    color: var(--text-white);
    overflow: hidden;
  }
  .brand {
    position: absolute;
    left: 110px;
    top: 62px;
    width: 930px;
    color: var(--brand-cyan);
    font-weight: 400;
    text-align: right;
  }
  .brand-name {
    display: block;
    font-size: 150px;
    line-height: 1;
    letter-spacing: 0.06em;
    text-align: center;
  }
  .brand-tagline {
    display: block;
    margin-top: 4px;
    font-size: 32px;
    line-height: 1;
    letter-spacing: 0.55em;
    margin-right: -0.55em;
  }
  .contact-person {
    position: absolute;
    right: 76px;
    top: 346px;
    text-align: right;
  }
  .person-name {
    margin: 0;
    font-size: 44px;
    font-weight: 700;
    line-height: 1.1;
  }
  .person-role {
    margin: 8px 0 0;
    font-size: 46px;
    font-weight: 400;
    line-height: 1.1;
  }
  .company-details,
  .direct-details {
    position: absolute;
    bottom: 28px;
    margin: 0;
    font-size: 41px;
    font-weight: 400;
    line-height: 72px;
    font-style: normal;
  }
  .company-details {
    left: 46px;
  }
  .direct-details {
    right: 76px;
    text-align: right;
  }
  .company-details span,
  .direct-details span {
    display: block;
    white-space: nowrap;
  }
</style>
</head>
<body>
  <main class="business-card">
    <div class="brand" aria-label="Velnuka Promotions">
      <span class="brand-name">VELNUKA</span>
      <span class="brand-tagline">PROMOTIONS</span>
    </div>

    <section class="contact-person">
      <h1 class="person-name">Daniel MARSH</h1>
      <p class="person-role">Director</p>
    </section>

    <address class="company-details">
      <span>48 St. ............................</span>
      <span>Toronto - CANADA</span>
      <span>T. 224870391 • F. 22417835 •</span>
      <span>w. www.velnuka.com</span>
    </address>

    <address class="direct-details">
      <span>d.marsh@velnuka.com</span>
      <span>056418273</span>
    </address>
  </main>
</body>
</html>
```